Social responsible Renewable Energy company

We at voltaQ are an independent power producer company founded in 2021 that handles large scale deployment of Renewable Energy and carbon neutral Energy as a service model. We offer turnkey solutions using solar panel systems and this could be incorporated in our business cards. You can also find our logo in the documents provided. Another key issue is that the business cards will be printed on recicled paper, not sure if this is a limitation in deciding the design. The recycled sign should also be added on the business card and stating that the paper used was recycled. Our website is www.myvoltaq.example. It should also be very professional, not too dreamy but still needs to capture your imagination. We are really excited to get your ideas !

Target Market(s)

Renewable Energy market

Contact Information for Business Card

The business card will be printed on recycled paper. Name of the company is voltaQ. Website is www.myvoltaq.example

Requirements
Nice to have
• Our motto: Powered by renewable, driven by people.

```html
<!DOCTYPE html>
<html lang="en">
<head>
<meta charset="utf-8">
<title>voltaQ business card</title>
<link href="https://fonts.googleapis.com/css2?family=Lato:wght@400;700;900&display=swap" rel="stylesheet">
<style>
  :root {
    --backdrop: #a9c8e3;
    --paper: #f7f7f6;
    --navy: #1f4f7e;
    --blue: #2b78c0;
    --blue-soft: #4a8fd0;
    --blue-deep: #1a5a94;
    --rule: #2c4f78;
    --eco-green: #2f7d45;
    --white: #ffffff;
  }
  * { margin: 0; padding: 0; box-sizing: border-box; }
  html, body {
    width: 1200px; height: 801px; overflow: hidden;
    background: var(--backdrop);
    font-family: "Lato", Arial, sans-serif;
  }
  .stage {
    position: relative; width: 1200px; height: 801px;
    display: flex; align-items: center; justify-content: center; gap: 48px;
  }
  .card {
    position: relative; width: 530px; height: 303px;
    border-radius: 3px; overflow: hidden;
    box-shadow: 0 14px 30px rgba(30, 60, 100, 0.25);
  }

  /* Front */
  .card-front { background: var(--paper); border-bottom: 5px solid var(--blue); }
  .brand-name {
    position: absolute; top: 34px; right: 38px;
    font-weight: 900; font-size: 58px; letter-spacing: 1px;
    color: var(--navy); line-height: 1;
  }
  .person { position: absolute; top: 78px; left: 40px; }
  .person-name { font-weight: 700; font-size: 22px; color: var(--navy); letter-spacing: 0.5px; }
  .person-role { font-weight: 400; font-size: 17px; color: var(--blue-soft); margin-top: -2px; }
  .divider {
    position: absolute; top: 132px; left: 40px; right: 40px;
    height: 1px; background: var(--rule);
  }
  .contact-list { position: absolute; top: 146px; left: 40px; list-style: none; }
  .contact-list li {
    display: flex; align-items: center; gap: 10px;
    font-size: 14px; color: var(--navy); margin-bottom: 5px;
  }
  .contact-list svg { width: 12px; height: 12px; fill: var(--blue-soft); }
  .service-line {
    position: absolute; top: 222px; left: 40px;
    font-weight: 700; font-size: 11.5px; letter-spacing: 2px;
    color: var(--blue-soft); line-height: 1.35; text-transform: uppercase;
  }
  .web-tab {
    position: absolute; bottom: 0; right: 92px;
    background: var(--blue); color: var(--white);
    font-size: 12px; letter-spacing: 2px; padding: 6px 14px 4px;
  }
  .eco-mark {
    position: absolute; bottom: 10px; right: 40px;
    width: 30px; height: 30px; border-radius: 50%; background: var(--eco-green);
  }

  /* Back */
  .card-back {
    background: linear-gradient(160deg, var(--blue-deep) 0%, var(--blue) 100%);
    color: var(--white);
  }
  .card-back .brand-name {
    top: 92px; left: 0; right: 0; text-align: center;
    font-size: 84px; color: var(--white);
  }
  .motto {
    position: absolute; bottom: 40px; left: 24px; right: 24px;
    display: flex; align-items: center; gap: 12px;
    font-weight: 700; font-size: 12px; letter-spacing: 2.4px; white-space: nowrap;
  }
  .motto::before, .motto::after {
    content: ""; flex: 1; height: 1px; background: rgba(255,255,255,0.8);
  }
</style>
</head>
<body>
<main class="stage">
  <section class="card card-front">
    <div class="brand-name">voltaQ</div>
    <div class="person">
      <div class="person-name">LOREM IPSUM</div>
      <div class="person-role">Founder</div>
    </div>
    <div class="divider"></div>
    <ul class="contact-list">
      <li><svg viewBox="0 0 24 24" aria-hidden="true"><path d="M6.6 10.8a15 15 0 0 0 6.6 6.6l2.2-2.2c.3-.3.7-.4 1-.2 1.1.4 2.3.6 3.6.6.6 0 1 .4 1 1V20c0 .6-.4 1-1 1C10.6 21 3 13.4 3 4c0-.6.4-1 1-1h3.5c.6 0 1 .4 1 1 0 1.3.2 2.5.6 3.6.1.3 0 .7-.2 1z"/></svg>000 000 0000</li>
      <li><svg viewBox="0 0 24 24" aria-hidden="true"><path d="M2 5h20v14H2z M3 6l9 7 9-7" /></svg>loremipsum@mail.example</li>
      <li><svg viewBox="0 0 24 24" aria-hidden="true"><circle cx="12" cy="12" r="10"/></svg>www.myvoltaq.example</li>
    </ul>
    <p class="service-line">We offer turnkey solutions using<br>solar panel systems</p>
    <div class="web-tab">www.myvoltaq.example</div>
    <div class="eco-mark" role="img" aria-label="Recycled paper certification badge"></div>
  </section>

  <section class="card card-back">
    <div class="brand-name">voltaQ</div>
    <p class="motto">POWERED BY RENEWABLE, DRIVEN BY PEOPLE</p>
  </section>
</main>
</body>
</html>
```